dealcraftmentor.com - Podcast Guest Marketing E-Flyer PDF

Dear Designers:I am in need of an attractive and attention-getting layout and design for a three-page marketing flyer (commonly known as a media one sheet) that will be sent via e-mail, as PDF file, to various Podcast hosts to market me as a guest on their podcasts. I want the design of the document to "mirror" the design and branding on my parent dealcraftmentor.com website. I am providing ALL the edited and proofread copy and content - the designer just needs to create the design for this marketing document. I want an active PDF document and icons should be used for WorkLoop, Phone, E-mail , and website- with hyperlinks that connect accordingly. I need a fast turnaround.
Updates

Dear Designers - instead of using the photo in the project file of me speaking to the audience for the banner image - I thought it would be a better idea to make this marketing piece specific to Podcast Hosts. Therefore, an image such as the one in the link below would be good to use for a banner image. https://www.pixelvarnow.com/find?q=podcast+studio+photos&mode=img&ref=univ&id=Qm7TzRk2LwPa9XcNvB4eHyU8sDjF1gA5oE3iKtZ6bW0nMh&w=1377&h=804#pic=vrolapemxq3BcT:

Target Market(s)

This PDF document will be sent to 650 Podcast hosts in North America via a broadcast e-mail.

Font styles to use
Sans Serif

Colors
ec1f27
ffffff
000000
333333
9d9d9d

Requirements
Must have
• A three-page layout that is easy to navigate in PDF form.
• Proper font styles and sizes for key emphasis areas on the document/
• Consistent branding to mirror my dealcraftmentor.com parent website
• Must be easy for people to read
• Attention-getting design elements and layout
• Professional and sophisticated design
• Icons for contact information
Should not have
• Should not be cluttered and junky-looking.
• Should not use small font sizes that makes it difficult to read.
• If Podcast hosts are interested in having me as a guest - they will read the content as required on three-pages

```html
<!DOCTYPE html>
<html lang="en">
<head>
<meta charset="utf-8">
<title>dealcraftmentor.com – Podcast Guest One Sheet</title>
<link href="https://fonts.googleapis.com/css2?family=Montserrat:wght@400;500;600;700&display=swap" rel="stylesheet">
<style>
:root{
  --red:#ec1f27;
  --white:#ffffff;
  --black:#000000;
  --ink:#333333;
  --grey:#9d9d9d;
  --stage:#dcd8d3;
}
*{margin:0;padding:0;box-sizing:border-box}
html,body{width:1200px;height:903px;overflow:hidden}
body{background:var(--stage);font-family:"Montserrat",Arial,sans-serif;color:var(--ink);position:relative}
.page{position:absolute;top:189px;width:371px;height:525px;background:var(--white);box-shadow:0 4px 14px rgba(0,0,0,.35);overflow:hidden}
.page--one{left:20px}
.page--two{left:414px}
.page--three{left:805px}
.abs{position:absolute}
.brand{left:0;right:0;top:20px;display:flex;justify-content:center;align-items:center;gap:5px}
.brand__mark{width:14px;height:14px;background:var(--red)}
.brand__name{font-size:15px;font-weight:500;color:var(--black);letter-spacing:-.2px}
.hero-photo{left:0;top:51px;width:371px;height:150px;background:linear-gradient(160deg,#8a8a8a 0%,#4a4a4a 55%,#2b2b2b 100%)}
.hero-band{left:0;top:201px;width:371px;height:66px;background:var(--red);color:var(--white);text-align:center;padding-top:9px}
.hero-band__title{font-size:10.5px;font-weight:700;line-height:13px}
.hero-band__lede{font-size:6.6px;font-weight:600;line-height:8.4px;margin-top:4px;padding:0 20px}
.section-title{color:var(--red);font-size:8.4px;font-weight:600;left:17px;right:17px}
.body-copy{left:17px;right:17px;font-size:4.8px;line-height:6.4px;text-align:justify;color:var(--ink)}
.body-copy p+p{margin-top:6px}
.numbered{list-style:none;counter-reset:n}
.numbered li{counter-increment:n;position:relative;padding-left:12px;margin-bottom:3.6px}
.numbered li::before{content:counter(n) ".";position:absolute;left:2px}
.footer{left:0;bottom:0;width:371px;height:26px;color:var(--white);font-size:7.2px;font-weight:500}
.footer svg.band{position:absolute;left:0;top:0}
.footer__item{position:absolute;top:0;height:26px;display:flex;align-items:center;gap:4px}
.footer__phone{left:20px;font-size:8.4px}
.footer__mail{left:132px}
.footer__web{left:238px}
.media-sub{left:17px;font-size:4.8px;font-weight:600;color:var(--ink)}
.media-row{left:30px;right:30px;display:flex;justify-content:space-between;align-items:center}
.media-name{font-size:11px;font-weight:700;color:var(--black)}
.media-name--red{color:var(--red)}
.media-name--blue{color:#1f4d8f}
.testimonial-head{left:21px;font-size:7.4px;font-weight:600;color:var(--black);line-height:10px}
.quote{position:absolute;border:1px solid var(--red);border-radius:4px;left:20px;width:331px}
.quote__open,.quote__close{position:absolute;color:var(--red);font-size:20px;font-weight:700;line-height:1;background:var(--white);padding:0 2px}
.quote__open{left:4px;top:-9px}
.quote__close{right:-4px;bottom:-11px}
.quote__text{font-size:5px;line-height:6.6px;font-style:italic;color:var(--ink);padding:12px 14px 0 14px;text-align:justify}
.quote__cite{font-size:4.6px;line-height:5.6px;font-weight:600;color:var(--black);padding:5px 0 0 154px}
.p3-head{left:17px;right:17px;top:32px;font-size:7.4px;font-weight:700;color:var(--black);line-height:10px}
.portrait{left:136px;top:306px;width:100px;height:100px;border-radius:50%;background:radial-gradient(circle at 50% 40%,#9a9a9a,#3a3a3a);border:3px solid #e2e2e2;box-shadow:0 0 0 1px #bdbdbd}
.signoff{left:0;right:0;top:418px;text-align:center;font-size:8.4px;line-height:10.4px;color:var(--black)}
.signoff strong{font-weight:600}
</style>
</head>
<body>

<!-- Page one -->
<section class="page page--one">
  <div class="abs brand"><span class="brand__mark"></span><span class="brand__name">dealcraftmentor</span></div>
  <div class="abs hero-photo" role="img" aria-label="Banner photo of a podcast studio with microphones"></div>
  <div class="abs hero-band">
    <div class="hero-band__title">Meet Dealcraft Mentor Daniel R. Vostrek –<br>The Expert You Need As a Guest on Your Podcast</div>
    <div class="hero-band__lede">Are you looking for a relevant and appealing topic and an engaging subject matter expert who can provide measurable value and life-changing tips to the listeners of your podcast?</div>
  </div>
  <h2 class="abs section-title" style="top:278px">Why Negotiating and Decision Making Should Be Topics on Your Podcast</h2>
  <div class="abs body-copy" style="top:291px">
    <p>Regardless of your podcast theme – it's important to remember that your listeners are negotiating all the time – in their personal lives, social lives, and especially in their business lives. Negotiating is an essential life skill. Everyone can improve his or her negotiating skills, and Daniel is the expert who can provide the answers your people crave. Your podcast listeners will benefit from Daniel's proven, practical, and relevant negotiating strategies and tips that will improve results and outcomes in all types of personal and business negotiations.</p>
  </div>
  <h2 class="abs section-title" style="top:334px">Six Reasons to Book Daniel R. Vostrek As a Guest on Your Podcast</h2>
  <ol class="abs body-copy numbered" style="top:348px">
    <li>Daniel is a dynamic, thought-provoking, engaging, captivating, and entertaining speaker who will share some great personal stories to help your listeners better understand and relate to the topic of negotiating and decision-making dynamics. He will indeed challenge the "status quo."</li>
    <li>Daniel is the founder of dealcraftmentor.com and is an internationally recognized expert and highly rated speaker on the topics of negotiating and decision-making dynamics that affect negotiated outcomes. His versatility and commitment to proper preparation will ensure that his content is tailored to address the theme of your podcast and the needs of your listeners.</li>
    <li>His five-star-rated presentations and training programs have been delivered around the world to small and medium-sized businesses, Top 500 corporations, and large industry, trade, and peer-to-peer associations such as Young Leaders' Network and Founders' Circle.</li>
    <li>Daniel has personally trained over 50,000 people of all experience levels, across multiple industries, in 31 countries how to negotiate more effectively.</li>
    <li>With formal training in broadcasting and media arts, Daniel provides 30 years of experience as a professional speaker who can provide your listeners with valuable insights, solutions, and answers to address listeners' challenges and questions.</li>
    <li>Daniel is the creator of the best-selling Deal Ready Toolkit Audio Learning Program – designed to be an effective all-in-one learning solution that helps people improve their negotiating capabilities and skills. He is also the host of his soon-to-be-launched Podcast – The Deal Table.</li>
  </ol>
  <footer class="abs footer">
    <svg class="band" width="371" height="26" viewBox="0 0 371 26" aria-hidden="true">
      <polygon points="0,0 117,0 125,26 0,26" fill="#000"/>
      <polygon points="122,0 371,0 371,26 130,26" fill="#ec1f27"/>
    </svg>
    <span class="footer__item footer__phone"><svg width="9" height="9" viewBox="0 0 24 24" aria-hidden="true"><path fill="#ec1f27" d="M6.6 10.8a15.1 15.1 0 006.6 6.6l2.2-2.2c.3-.3.7-.4 1-.2 1.1.4 2.300.6 3.6.6.6 0 1 .4 1 1V20c0 .6-.4 1-1 1A17 17 0 013 4c0-.6.4-1 1-1h3.5c.6 0 1 .4 1 1 0 1.2.2 2.4.6 3.6.1.3 0 .7-.2 1z"/></svg>555-014-2290</span>
    <span class="footer__item footer__mail"><svg width="8" height="6" viewBox="0 0 16 12" aria-hidden="true"><rect width="16" height="12" fill="#fff"/><path d="M0 0l8 6 8-6" fill="none" stroke="#ec1f27" stroke-width="1.5"/></svg>daniel@vostrek.com</span>
    <span class="footer__item footer__web"><svg width="7" height="7" viewBox="0 0 12 12" aria-hidden="true"><circle cx="6" cy="6" r="5.5" fill="#fff"/><circle cx="6" cy="6" r="2.2" fill="#ec1f27"/></svg>www.dealcraftmentor.com</span>
  </footer>
</section>

<!-- Page two -->
<section class="page page--two">
  <h2 class="abs section-title" style="top:18px">How Podcast Listeners Will Benefit</h2>
  <div class="abs body-copy" style="top:33px">
    <p>Most people are intimidated by the prospect and process of negotiating – and often view negotiating as an uncomfortable haggling and bargaining process that may involve confrontation, anxiety, and stress.</p>
    <p>If podcast listeners are like most people – then they probably are concerned about being taken advantage of – or that they are missing out on potential opportunities in their personal, social, and business negotiations.</p>
    <p>To alleviate your listeners' concerns, Daniel will provide them with easy-to-understand negotiating strategies, tactics, phrases, and tips they can immediately apply – the moment the podcast episode ends. Your listeners will feel more confident when they are equipped with the powerful and beneficial strategies &amp; techniques that will help them save/make money &amp; arrive at better outcomes when negotiating with customers, clients, suppliers, contractors, financial institutions, retailers, co-workers, colleagues, and family members.</p>
  </div>
  <h2 class="abs section-title" style="top:126px">Daniel R. Vostrek in the Media</h2>
  <div class="abs media-sub" style="top:139px">Daniel has appeared on radio programs, written articles or contributed to articles for the following media outlets:</div>
  <div class="abs media-row" style="top:159px">
    <span class="media-name media-name--blue">Ledger Daily</span>
    <span class="media-name media-name--blue">Venture Hall</span>
    <span class="media-name media-name--blue">Capital Weekly</span>
    <span class="media-name">MARGIN</span>
  </div>
  <div class="abs media-row" style="top:192px;left:55px;right:75px">
    <span class="media-name media-name--red">The Northern Post</span>
    <span class="media-name media-name--red">Pitch Quarterly</span>
  </div>
  <h2 class="abs section-title" style="top:234px">Three Ways You Can Profit From Booking Daniel R. Vostrek on Your Podcast</h2>
  <div class="abs body-copy" style="top:249px;font-weight:600">Upon mutual agreement, podcast hosts and listeners can have access to the following money-saving &amp; profit-generating opportunities:</div>
  <ol class="abs body-copy numbered" style="top:271px">
    <li>Podcast hosts will be provided with a specific promotional code to share with your listeners that will entitle them to receive a special one-time discount of $19.95US off the purchase of the MP3 download of the Deal Ready Toolkit Audio Learning Program available on my online store. Complete download and purchase instructions will be provided to podcast hosts to publish in your notes and also communicate to your listeners.</li>
    <li>Podcast hosts will receive a 10% commission payable on the net sales dollar revenue generated from the sale of MP3 downloads of Daniel's Deal Ready Toolkit Audio Learning Program.</li>
    <li>Podcast hosts will receive a 10% referral fee for any corporation or association that books Daniel for a presentation, seminar, or learning workshop that directly results from my participation on your podcast.</li>
  </ol>
  <div class="abs body-copy" style="top:348px">Note: Discount and commission payments are subject to agreement to standard terms and conditions.</div>
  <div class="abs testimonial-head" style="top:372px">Testimonials:<br>What Some Clients Are Saying About the Dealcraft Mentor</div>
  <div class="quote" style="top:407px;height:83px">
    <span class="quote__open">“</span>
    <p class="quote__text">Daniel Vostrek did a terrific job on my podcast. His negotiating insights and tips were well received by my listeners, and he was an engaging, knowledgeable, and entertaining guest. Given my expertise in real estate, I thought I was a good negotiator – until Daniel taught me a few new strategies and tips during the podcast. I would recommend Daniel to any podcast host – he is a pro and his topics are relevant and can benefit everyone.</p>
    <p class="quote__cite">Carl Bennick<br>Podcast Host<br>Property Growth Roundtable Podcast, Millbrook, Texas</p>
    <span class="quote__close">”</span>
  </div>
  <footer class="abs footer">
    <svg class="band" width="371" height="26" viewBox="0 0 371 26" aria-hidden="true">
      <polygon points="0,0 117,0 125,26 0,26" fill="#000"/>
      <polygon points="122,0 371,0 371,26 130,26" fill="#ec1f27"/>
    </svg>
    <span class="footer__item footer__phone"><svg width="9" height="9" viewBox="0 0 24 24" aria-hidden="true"><path fill="#ec1f27" d="M6.6 10.8a15.1 15.1 0 006.6 6.6l2.2-2.2c.3-.3.7-.4 1-.2 1.1.4 2.3.6 3.6.6.6 0 1 .4 1 1V20c0 .6-.4 1-1 1A17 17 0 013 4c0-.6.4-1 1-1h3.5c.6 0 1 .4 1 1 0 1.2.2 2.4.6 3.6.1.3 0 .7-.2 1z"/></svg>555-014-2290</span>
    <span class="footer__item footer__mail"><svg width="8" height="6" viewBox="0 0 16 12" aria-hidden="true"><rect width="16" height="12" fill="#fff"/><path d="M0 0l8 6 8-6" fill="none" stroke="#ec1f27" stroke-width="1.5"/></svg>daniel@vostrek.com</span>
    <span class="footer__item footer__web"><svg width="7" height="7" viewBox="0 0 12 12" aria-hidden="true"><circle cx="6" cy="6" r="5.5" fill="#fff"/><circle cx="6" cy="6" r="2.2" fill="#ec1f27"/></svg>www.dealcraftmentor.com</span>
  </footer>
</section>

<!-- Page three -->
<section class="page page--three">
  <h2 class="abs p3-head">Below is a partial listing of testimonials from attendees at a Founders' Circle (FC) event provided by the RT Kessling, Chapter Learning Chair:</h2>
  <div class="quote" style="top:66px;height:40px">
    <span class="quote__open">“</span>
    <p class="quote__text">A very engaging, entertaining, and inspirational speaker who provided very useful information, strategies, and tips to apply to all my future negotiations.</p>
    <span class="quote__close">”</span>
  </div>
  <div class="quote" style="top:130px;height:38px">
    <span class="quote__open">“</span>
    <p class="quote__text">Thank you to FC Western New York for booking this speaker! I learned some things that I can address immediately and a lot material that I need to practice. Great session!</p>
    <span class="quote__close">”</span>
  </div>
  <div class="quote" style="top:192px;height:38px">
    <span class="quote__open">“</span>
    <p class="quote__text">Daniel was an outstanding speaker on the topic of negotiating! He was one of my favorite speakers ever! Daniel was a real 'teacher' versus other typical speakers who spend two hours bragging or promoting their book.</p>
    <span class="quote__close">”</span>
  </div>
  <div class="quote" style="top:251px;height:40px">
    <span class="quote__open">“</span>
    <p class="quote__text">Daniel was a very knowledgeable and well-prepared speaker who provided helpful tips and scripts throughout the entire presentation! I would love to learn more from this speaker.</p>
    <span class="quote__close">”</span>
  </div>
  <div class="abs portrait" role="img" aria-label="Black and white portrait photo of the chapter learning chair"></div>
  <div class="abs signoff"><strong>RT Kessling, CEO and President</strong><br>Brightfold Document Services<br>Founders' Circle (FC) Western New York<br>Learning Chair</div>
  <footer class="abs footer">
    <svg class="band" width="371" height="26" viewBox="0 0 371 26" aria-hidden="true">
      <polygon points="0,0 117,0 125,26 0,26" fill="#000"/>
      <polygon points="122,0 371,0 371,26 130,26" fill="#ec1f27"/>
    </svg>
    <span class="footer__item footer__phone"><svg width="9" height="9" viewBox="0 0 24 24" aria-hidden="true"><path fill="#ec1f27" d="M6.6 10.8a15.1 15.1 0 006.6 6.6l2.2-2.2c.3-.3.7-.4 1-.2 1.1.4 2.3.6 3.6.6.6 0 1 .4 1 1V20c0 .6-.4 1-1 1A17 17 0 013 4c0-.6.4-1 1-1h3.5c.6 0 1 .4 1 1 0 1.2.2 2.4.6 3.6.1.3 0 .7-.2 1z"/></svg>555-014-2290</span>
    <span class="footer__item footer__mail"><svg width="8" height="6" viewBox="0 0 16 12" aria-hidden="true"><rect width="16" height="12" fill="#fff"/><path d="M0 0l8 6 8-6" fill="none" stroke="#ec1f27" stroke-width="1.5"/></svg>daniel@vostrek.com</span>
    <span class="footer__item footer__web"><svg width="7" height="7" viewBox="0 0 12 12" aria-hidden="true"><circle cx="6" cy="6" r="5.5" fill="#fff"/><circle cx="6" cy="6" r="2.2" fill="#ec1f27"/></svg>www.dealcraftmentor.com</span>
  </footer>
</section>

</body>
</html>
```